Machining Business Order Thank You Insert

I am looking for a business style card to include with orders that I ship. The card needs to thank the recipient for their order, and encourage them to leave a review. The card should include my business name and contact information and have an area to hand write a message.

I mainly sale on Crafvine and my own website. We are a machining an manufacturing business that are in the sale of mostly metal machined and 3d printed plastic products.

The front of the card should include the following:
Logo: (attached)
Snapgrid: https://www.instagram.com/quillforge/
Friendwall: https://www.facebook.com/QuillForge
Website: https://www.quillforge-example.com/

The back of the card needs an area to write a message

Industry/Entity Type

3D Printing, Machining, Crafvine

Contact Information for Business Card

Black or white front, white back to write a personal message

Font styles to use
Sans Serif

Colors

Designer to choose colors to be used in the design.

Requirements
Must have
• Encourage a review, social media info

```html
<!DOCTYPE html>
<html lang="en">
<head>
<meta charset="utf-8">
<title>QuillForge Order Insert</title>
<link href="https://fonts.googleapis.com/css2?family=Lato:wght@400;700&display=swap" rel="stylesheet">
<style>
  :root {
    --backdrop: #262626;
    --card-grey: #6b6b6e;
    --panel-white: #ffffff;
    --accent: #f05a24;
    --ink: #2b2b2b;
    --text-light: #ffffff;
    --rule: #3a3a3a;
  }
  * { box-sizing: border-box; margin: 0; padding: 0; }
  html, body { width: 1200px; height: 1080px; overflow: hidden; }
  body {
    background: var(--backdrop);
    font-family: "Lato", sans-serif;
    display: flex;
    flex-direction: column;
    align-items: center;
    justify-content: center;
    gap: 40px;
  }
  .card {
    position: relative;
    width: 840px;
    height: 480px;
    border-radius: 18px;
    background: var(--card-grey);
    overflow: hidden;
  }
  .brand {
    display: flex;
    align-items: center;
    gap: 14px;
  }
  .brand-mark {
    width: 22px;
    height: 22px;
    background: var(--accent);
    flex: none;
  }
  .brand-name {
    font-size: 26px;
    font-weight: 400;
    letter-spacing: 8px;
    color: var(--text-light);
    text-transform: uppercase;
  }

  /* Message side */
  .card--message .brand {
    position: absolute;
    left: 48px;
    top: 210px;
    flex-direction: column;
    align-items: flex-start;
    gap: 16px;
  }
  .card--message .brand-name { font-size: 22px; letter-spacing: 6px; }
  .message-panel {
    position: absolute;
    right: 40px;
    top: 40px;
    width: 480px;
    height: 400px;
    background: var(--panel-white);
    border-radius: 34px;
    padding: 52px 44px 36px;
    display: flex;
    flex-direction: column;
  }
  .message-label {
    color: var(--accent);
    font-size: 24px;
    font-weight: 700;
    margin-bottom: 8px;
  }
  .write-line {
    border-bottom: 2px dashed var(--rule);
    height: 56px;
  }
  .panel-url {
    margin-top: auto;
    align-self: flex-end;
    font-size: 22px;
    color: var(--ink);
  }
  .panel-url .hl { color: var(--accent); }

  /* Front side */
  .card--front .brand {
    position: absolute;
    left: 64px;
    top: 56px;
  }
  .thanks {
    position: absolute;
    left: 64px;
    top: 116px;
    width: 700px;
  }
  .thanks-title {
    color: var(--text-light);
    font-size: 30px;
    font-weight: 700;
  }
  .thanks-note {
    margin-top: 8px;
    color: var(--text-light);
    font-size: 22px;
  }
  .thanks-note .hl { color: var(--accent); font-weight: 700; }
  .follow-title {
    position: absolute;
    left: 64px;
    top: 232px;
    color: var(--accent);
    font-size: 26px;
    letter-spacing: 1px;
  }
  .social-list {
    position: absolute;
    left: 64px;
    top: 286px;
    list-style: none;
    display: flex;
    flex-direction: column;
    gap: 18px;
  }
  .social-item {
    display: flex;
    align-items: center;
    gap: 16px;
    color: var(--text-light);
    font-size: 26px;
  }
  .social-item .hl { color: var(--accent); }
  .social-dot { width: 24px; height: 24px; flex: none; }
</style>
</head>
<body>

  <section class="card card--message" aria-label="Message side">
    <div class="brand">
      <span class="brand-mark"></span>
      <span class="brand-name">QuillForge</span>
    </div>
    <div class="message-panel">
      <p class="message-label">Your Message Here :</p>
      <div class="write-line"></div>
      <div class="write-line"></div>
      <div class="write-line"></div>
      <div class="write-line"></div>
      <p class="panel-url">www.<span class="hl">quillforge-example</span>.com</p>
    </div>
  </section>

  <section class="card card--front" aria-label="Front side">
    <div class="brand">
      <span class="brand-mark"></span>
      <span class="brand-name">QuillForge</span>
    </div>
    <div class="thanks">
      <p class="thanks-title">Thank you for your order!</p>
      <p class="thanks-note">Loved it? Please leave us a review on <span class="hl">Crafvine</span>.</p>
    </div>
    <p class="follow-title">FOLLOW &nbsp;US ON :-</p>
    <ul class="social-list">
      <li class="social-item">
        <svg class="social-dot" viewBox="0 0 24 24"><circle cx="12" cy="12" r="11" fill="#f05a24"/></svg>
        <span>www.friendwall.com/QuillForge</span>
      </li>
      <li class="social-item">
        <svg class="social-dot" viewBox="0 0 24 24"><circle cx="12" cy="12" r="11" fill="#f05a24"/></svg>
        <span>www.snapgrid.com/quillforge/</span>
      </li>
      <li class="social-item">
        <svg class="social-dot" viewBox="0 0 24 24"><circle cx="12" cy="12" r="11" fill="#f05a24"/></svg>
        <span>www.<span class="hl">quillforge-example</span>.com</span>
      </li>
    </ul>
  </section>

</body>
</html>
```